" A empresa irá atuar no Ramo de Crédito Imobiliário, prestando serviço complementar à Vale Norte Soluções Imobiliárias, empresa de intermediaçao imobiliária que atua no Centro-Oeste. "

```html
<!DOCTYPE html>
<html lang="pt-BR">
<head>
<meta charset="UTF-8">
<title>Crachá — Vértice Crédito</title>
<link href="https://fonts.googleapis.com/css2?family=Roboto:wght@400;500;700&display=swap" rel="stylesheet">
<style>
  :root{
    --navy:#1c2f5e;
    --gold:#d9a62e;
    --white:#ffffff;
    --ink:#3d4150;
    --muted:#6a6f7d;
    --backdrop:#e8e5e0;
    --field-line:#4a4f5c;
  }
  *{box-sizing:border-box;margin:0;padding:0}
  html,body{width:1200px;height:1200px;overflow:hidden}
  body{background:var(--backdrop);font-family:"Roboto",Arial,sans-serif;position:relative}
  .badge{position:absolute;top:247px;width:440px;height:720px;border-radius:30px;overflow:hidden}
  .badge--front{left:170px;background:var(--navy);color:var(--white)}
  .badge--back{left:650px;background:var(--white);color:var(--ink)}
  .lanyard-slot{position:absolute;top:30px;left:50%;transform:translateX(-50%);width:72px;height:22px;border-radius:11px;background:var(--backdrop)}
  .badge--front .lanyard-slot{border:3px solid #15244a}
  .badge--back .lanyard-slot{border:3px solid #9a9da5}
  .brand{position:absolute;top:138px;left:0;right:0;text-align:center}
  .brand__name{font-weight:700;font-size:48px;letter-spacing:1px;line-height:1;text-transform:uppercase}
  .brand__tagline{margin-top:10px;font-size:13px;font-weight:500;letter-spacing:7px;text-transform:uppercase}
  .badge--front .brand__name{color:var(--white)}
  .badge--front .brand__tagline{color:var(--gold)}
  .badge--back .brand__name{color:var(--navy)}
  .badge--back .brand__tagline{color:var(--navy)}
  .portrait{position:absolute;top:257px;left:50%;transform:translateX(-50%);width:218px;height:260px;border:6px solid var(--gold);border-radius:14px;background:linear-gradient(160deg,#cfd8d4 0%,#e7e2dc 55%,#f4f4f2 100%)}
  .holder{position:absolute;top:540px;left:0;right:0;text-align:center}
  .holder__name{font-size:26px;font-weight:500}
  .holder__role{font-size:25px;font-weight:400;margin-top:4px}
  .swoosh{position:absolute;left:0;bottom:0;width:440px;height:240px}
  .fields{position:absolute;top:250px;left:38px;right:38px}
  .field{height:46px;border:2px solid var(--field-line);border-radius:10px;padding:0 12px;display:flex;align-items:center;font-size:20px;color:var(--ink);margin-bottom:14px}
  .field--notes{height:166px;margin-top:38px}
  .contact{position:absolute;top:620px;left:0;right:0;text-align:center;font-size:19px;line-height:24px;color:var(--muted)}
  .contact__web{color:var(--ink);font-weight:500}
</style>
</head>
<body>
  <section class="badge badge--front">
    <div class="lanyard-slot"></div>
    <div class="brand">
      <div class="brand__name">Vértice Crédito</div>
      <div class="brand__tagline">Crédito Imobiliário</div>
    </div>
    <div class="portrait" role="img" aria-label="Foto do colaborador"></div>
    <div class="holder">
      <div class="holder__name">Nome Sobrenome</div>
      <div class="holder__role">Cargo</div>
    </div>
    <svg class="swoosh" viewBox="0 0 440 240" aria-hidden="true">
      <path d="M0 240 V190 C170 180 360 120 440 40 V240 Z" fill="var(--gold)"/>
      <path d="M0 186 C170 176 360 116 440 36" fill="none" stroke="var(--white)" stroke-width="4"/>
    </svg>
  </section>

  <section class="badge badge--back">
    <div class="lanyard-slot"></div>
    <div class="brand">
      <div class="brand__name">Vértice Crédito</div>
      <div class="brand__tagline">Crédito Imobiliário</div>
    </div>
    <div class="fields">
      <div class="field">Nome:</div>
      <div class="field">CPF:</div>
      <div class="field field--notes"></div>
    </div>
    <div class="contact">
      <p>Av. Nome da Avenida, 00 - Centro São Paulo-SP</p>
      <p>(11) 0000-0000 / 0000-0000</p>
      <p>contato@verticecredito.com.br</p>
      <p class="contact__web">www.verticecredito.com.br</p>
    </div>
  </section>
</body>
</html>
```